Stationery Design Project

KT7 Staffing requires letterhead and business card designs for a company based in London. Just like the name, we're a management resourcing company, providing resources to third party companies. You can see www.kt7staffing-example.com for ideas on existing colour schemes and design concepts that have been implimented and agreed to. Ultimately the design should broadcast professionalism, safety and the concept of growth.

Target Market(s)

Financial institutes; friendly societies (All UK based)

Industry/Entity Type

Safety

Requirements
Must have
• Files produced should be print ready; and the text in them editable (eg address, name etc)

```html
<!DOCTYPE html>
<html lang="en">
<head>
<meta charset="utf-8">
<title>KT7 Staffing – Stationery</title>
<link rel="stylesheet" href="https://fonts.googleapis.com/css2?family=Roboto+Condensed:wght@400;700&family=Jost:wght@400;500&display=swap">
<style>
  :root {
    --backdrop: #1c1c1c;
    --paper: #ffffff;
    --ink: #2b2b2b;
    --teal: #1f9aaa;
    --teal-dark: #178a99;
    --sky: #74bcdb;
    --card-text: #ffffff;
  }
  * { box-sizing: border-box; margin: 0; padding: 0; }
  html, body { width: 1200px; height: 1091px; overflow: hidden; }
  body {
    background: radial-gradient(circle at 50% 40%, #2e2e2e, var(--backdrop) 75%);
    font-family: "Roboto Condensed", "Arial Narrow", sans-serif;
    color: var(--ink);
    position: relative;
  }

  /* Letterhead */
  .letterhead {
    position: absolute; left: 60px; top: 60px;
    width: 620px; height: 877px;
    background: var(--paper);
    padding: 44px 48px;
  }
  .letterhead-top { display: flex; justify-content: space-between; align-items: flex-start; }
  .brand {
    display: flex; align-items: center; gap: 10px;
    font-family: "Jost", sans-serif; font-weight: 500;
    color: var(--teal); font-size: 34px; line-height: 1;
  }
  .brand-mark { width: 14px; height: 14px; background: var(--teal); }
  .contact-list { font-size: 11.5px; line-height: 1.45; }
  .contact-list dt { display: inline; font-weight: 700; }
  .contact-list dd { display: inline; margin-left: 3px; }
  .contact-list dd::after { content: "\A"; white-space: pre; }

  .letter-body { margin-top: 110px; font-size: 13.5px; line-height: 1.95; }
  .letter-body p + p { margin-top: 14px; }
  .salutation { line-height: 2; }
  .sign-off { margin-top: 44px; text-align: right; font-size: 13.5px; line-height: 2; }

  /* Business cards */
  .card {
    position: absolute; left: 730px; width: 410px; height: 230px;
    background: var(--paper); border-radius: 14px; overflow: hidden;
  }
  .card-front { top: 220px; display: flex; }
  .card-back { top: 490px; display: flex; align-items: center; justify-content: center; }
  .card-front .brand-side { flex: 1; display: flex; align-items: center; justify-content: center; }
  .card-front .brand { font-size: 22px; gap: 8px; }
  .card-front .brand-mark { width: 10px; height: 10px; }
  .card-back .brand { font-size: 36px; }
  .info-side { width: 200px; display: flex; flex-direction: column; font-family: "Jost", sans-serif; color: var(--card-text); }
  .name-panel { background: var(--sky); height: 110px; padding: 22px 26px; }
  .person-name { font-size: 15px; }
  .person-role { font-size: 10px; opacity: .9; margin-top: 2px; }
  .details-panel { flex: 1; background: var(--teal-dark); margin-top: 3px; padding: 10px 26px; font-size: 10.5px; line-height: 1.55; }
</style>
</head>
<body>

<article class="letterhead">
  <header class="letterhead-top">
    <div class="brand"><span class="brand-mark"></span>KT7 Staffing</div>
    <dl class="contact-list">
      <dt>Phone :</dt><dd>123 456 789</dd>
      <dt>Fax :</dt><dd>123 456 789</dd>
      <dt>Email :</dt><dd>yourname@kt7staffing-example.com</dd>
      <dt>Website :</dt><dd>www.kt7staffing-example.com</dd>
    </dl>
  </header>

  <section class="letter-body">
    <p class="salutation">Dear<br>Sir/Madam<br>Its all sample text<br>
    Through a dedicated team of professionals, with at least fifteen years of experience in their various fields, we offer clients a focused service of problem solving, key consultation and driving change for all of the challenges in their business.</p>
    <p>Our unique approach means that our team of professionals work from the inside. They see the problems from the ground floor and are able to offer tailored advice on a range of business issues.</p>
    <p>KT7 Staffing is a multi-national company with clients in North America, Europe and Africa. We hire only professionals with at least 10 - 15 years of experience in their relevant fields. All of whom exemplify our core business values – Professionalism, Talent, Integrity and Loyalty.</p>
    <p>Our professionals are guided by the innovative culture at KT7 Staffing, a culture which puts great emphasis on teamwork, results and flexibility. When our team of professionals go inside any business they do so with an open mind, ready to address any multitude of issues that may present themselves.</p>
    <p>Our custom approach is unique to each of our clients, ensuring the each client receives the best service.</p>
  </section>

  <footer class="sign-off">Best regards<br>KT7 STAFFING</footer>
</article>

<section class="card card-front">
  <div class="brand-side">
    <div class="brand"><span class="brand-mark"></span>KT7 Staffing</div>
  </div>
  <div class="info-side">
    <div class="name-panel">
      <div class="person-name">Dorian Vell</div>
      <div class="person-role">Manager</div>
    </div>
    <div class="details-panel">
      1-800-555-0142<br>
      Facsimile: 818-555-0199<br>
      48 Harlow Lane #12<br>
      Kestrel, CA 90000<br>
      d.vell@kt7staffing-example.com<br>
      www.kt7staffing-example.com
    </div>
  </div>
</section>

<section class="card card-back">
  <div class="brand"><span class="brand-mark"></span>KT7 Staffing</div>
</section>

</body>
</html>
```